Thriving Mexican import business needs a new business card

Need a refresher of our current business card. Looking for a lighter background with the logo on one side. We will want this file to be adjustable so we can change names, emails and mobile numbers.
We are open to ideas but maintaining a professional image is critical.
Thankyou,

Target Market(s)

Anyone in food industry

Industry/Entity Type

Wholesale

Contact Information for Business Card

Mark Vellanoweth
Director
Corvan Products & Liquor Pty Ltd
5B Larkfield Ct, Brimsworth VIC 3051
0491325067 (03) 95147286
mark@corvanimports.com.au
corvanimportedgoodsandspirits.com.au

Font styles to use
Serif
Other font styles liked:
• NeoGram Heavy

Requirements
Must have
• Professional yet memorable
Corvan logo
Nice to have
• Chilli or tequila/mexican food pictures
Should not have
• Dark background

```html
<!DOCTYPE html>
<html lang="en">
<head>
<meta charset="utf-8">
<title>Corvan Products &amp; Liquor – Business Card</title>
<link href="https://fonts.googleapis.com/css2?family=Zilla+Slab:wght@400;700&display=swap" rel="stylesheet">
<style>
  :root {
    --backdrop: #c8c8c8;
    --card: #fdf1e6;
    --ink: #121214;
    --detail: #4a4a4a;
    --rule: #2a2a2a;
  }
  * { box-sizing: border-box; margin: 0; padding: 0; }
  html, body {
    width: 1125px; height: 1200px; overflow: hidden;
    background: var(--backdrop);
  }
  .canvas { position: relative; width: 1125px; height: 1200px; }
  .card {
    position: absolute; left: 178px; width: 768px; height: 437px;
    background: var(--card); border-radius: 18px;
    font-family: "Zilla Slab", Georgia, serif;
    color: var(--ink);
  }
  .card--front { top: 140px; }
  .card--back { top: 626px; }

  .brand {
    position: absolute; display: flex; flex-direction: column; align-items: center;
  }
  .brand__mark {
    width: 14px; height: 14px; background: var(--ink); margin-bottom: 12px;
  }
  .brand__name {
    font-weight: 700; letter-spacing: 2px; text-transform: uppercase; line-height: 1;
  }
  .card--front .brand { left: 160px; top: 156px; width: 190px; }
  .card--front .brand__name { font-size: 46px; }
  .card--back .brand { left: 0; right: 0; top: 172px; }
  .card--back .brand__mark { width: 20px; height: 20px; margin-bottom: 18px; }
  .card--back .brand__name { font-size: 76px; letter-spacing: 3px; }

  .divider {
    position: absolute; left: 384px; top: 134px; width: 1px; height: 169px;
    background: var(--rule);
  }
  .contact { position: absolute; left: 420px; top: 130px; color: var(--detail); }
  .contact__name { font-size: 21px; font-weight: 700; color: var(--ink); line-height: 1.1; }
  .contact__role { font-size: 14.5px; line-height: 1.2; margin-bottom: 9px; }
  .contact__address { font-size: 14.5px; line-height: 20px; margin-bottom: 8px; }
  .contact__list { list-style: none; }
  .contact__item {
    display: flex; align-items: center; gap: 6px;
    font-size: 14.5px; line-height: 20.5px;
  }
  .contact__icon { width: 11px; height: 11px; fill: var(--ink); flex: none; }
</style>
</head>
<body>
<main class="canvas">
  <section class="card card--front">
    <div class="brand">
      <span class="brand__mark"></span>
      <span class="brand__name">Corvan</span>
    </div>
    <div class="divider"></div>
    <div class="contact">
      <p class="contact__name">Mark Vellanoweth</p>
      <p class="contact__role">Director</p>
      <p class="contact__address">5B Larkfield Ct,<br>Brimsworth VIC 3051</p>
      <ul class="contact__list">
        <li class="contact__item">
          <svg class="contact__icon" viewBox="0 0 12 12"><path d="M2.5 0.5l2 2.3-1 1.3c.7 1.6 2 2.9 3.6 3.6l1.3-1 2.3 2-1.2 1.9C5 10.6 1.3 6.9.6 1.7z"/></svg>
          <span>0491325067</span>
        </li>
        <li class="contact__item">
          <svg class="contact__icon" viewBox="0 0 12 12"><path d="M3 0h6a1 1 0 0 1 1 1v10a1 1 0 0 1-1 1H3a1 1 0 0 1-1-1V1a1 1 0 0 1 1-1zm.6 1.3v8.2h4.8V1.3zM6 10.2a.6.6 0 1 0 0 1.2.6.6 0 0 0 0-1.2z"/></svg>
          <span>(03) 95147286</span>
        </li>
        <li class="contact__item">
          <svg class="contact__icon" viewBox="0 0 12 12"><path d="M0 2h12v8H0zm1.2 1l4.8 3.6L10.8 3z"/></svg>
          <span>mark@corvanimports.com.au</span>
        </li>
        <li class="contact__item">
          <svg class="contact__icon" viewBox="0 0 12 12"><circle cx="6" cy="6" r="5.5"/><path d="M3 3.5c1 0 1.5.8 1.2 1.6-.4.9.6 1.3.4 2.3L4 9.5 2.2 7.8 1.8 5z M8 2c-.5 1 .4 1.4 1.3 1.6l.8 2.2-1.5 1.3L7.5 6z" fill="#fdf1e6"/></svg>
          <span>corvanimportedgoodsandspirits.com.au</span>
        </li>
      </ul>
    </div>
  </section>

  <section class="card card--back">
    <div class="brand">
      <span class="brand__mark"></span>
      <span class="brand__name">Corvan</span>
    </div>
  </section>
</main>
</body>
</html>
```